Garden of Eden - Digital Party Invite

I'm throwing a Halloween party with the theme "Garden of Eden". The invite will be sent via Tidewell Cards. I need a custom design for the invite. Here are the details:
The image needs to be 670x970.
Needs to be sexy - maybe with Adam & Eve, and the snake w/the apple, etc
Text should be:
You Are Invited To
The Garden of Eden
Sat Oct 26 7:00PM
at
Dinah & Tobias's Home
612 North Birch Rd 7B
Costumes Highly Encouraged
Adults Only Please

```html
<!DOCTYPE html>
<html lang="en">
<head>
<meta charset="utf-8">
<title>The Garden of Eden – Party Invitation</title>
<link rel="stylesheet" href="https://fonts.googleapis.com/css2?family=Montserrat:wght@400;600&family=Playfair+Display:wght@700&display=swap">
<style>
  :root {
    --page-bg: #e6e4e1;
    --card-cream: #f6f1e7;
    --ink-pink: #e2548d;
    --ink-pink-soft: #e57aa3;
    --flora-rose: #eab1b8;
    --flora-green: #b9cfa8;
    --flora-gold: #f2cf86;
    --flora-violet: #c4b3d6;
    --scene-leaf: #7fa56a;
    --scene-sky: #cfe0dc;
  }
  * { box-sizing: border-box; margin: 0; padding: 0; }
  html, body {
    width: 1200px; height: 1200px; overflow: hidden;
    background: var(--page-bg);
  }
  .invite {
    position: absolute;
    left: 206px; top: 30px;
    width: 788px; height: 1140px;
    background: var(--card-cream);
    overflow: hidden;
    box-shadow: 0 2px 10px rgba(0,0,0,0.12);
  }
  .floral-border {
    position: absolute; inset: 0;
    background:
      radial-gradient(ellipse 46% 44% at 50% 52%, var(--card-cream) 70%, rgba(246,241,231,0) 100%),
      linear-gradient(180deg, var(--flora-rose) 0%, var(--flora-gold) 30%, var(--flora-violet) 55%, var(--flora-green) 80%, var(--flora-rose) 100%);
    opacity: 0.85;
  }
  .eden-frame {
    position: absolute;
    left: 234px; top: 245px;
    width: 321px; height: 175px;
    border: 1.5px solid var(--ink-pink);
    padding: 6px;
    background: var(--card-cream);
  }
  .eden-scene {
    width: 100%; height: 100%;
    background: linear-gradient(180deg, var(--scene-sky) 0%, var(--scene-leaf) 45%, #6f9656 100%);
  }
  .invite-text {
    position: absolute; left: 0; right: 0; top: 494px;
    text-align: center;
    color: var(--ink-pink);
    font-family: "Montserrat", sans-serif;
  }
  .lead-in {
    font-size: 19px; font-weight: 400; letter-spacing: 1px;
    color: var(--ink-pink-soft);
  }
  .event-title {
    margin-top: 6px;
    font-family: "Playfair Display", serif;
    font-weight: 700; font-size: 55px; line-height: 68px;
    letter-spacing: 0.5px;
  }
  .details { margin-top: 28px; font-size: 18px; line-height: 26px; }
  .details .strong { font-weight: 600; }
  .details .plain { color: var(--ink-pink-soft); font-weight: 400; font-size: 19px; }
  .notes { margin-top: 36px; font-size: 16px; line-height: 23px; letter-spacing: 0.3px; }
  .notes .strong { font-weight: 600; }
  .notes .plain { color: var(--ink-pink-soft); }
</style>
</head>
<body>
  <main class="invite">
    <div class="floral-border" role="img" aria-label="Watercolour wildflower border in pink, gold, violet and green framing the card"></div>

    <div class="eden-frame">
      <div class="eden-scene" role="img" aria-label="Illustration of Adam and Eve beneath an apple tree with the serpent coiled around its trunk"></div>
    </div>

    <section class="invite-text">
      <p class="lead-in">YOU ARE INVITED TO</p>
      <h1 class="event-title">THE GARDEN<br>OF EDEN</h1>
      <div class="details">
        <p class="strong">SAT OCT 26 7:00PM</p>
        <p class="plain">at</p>
        <p class="strong">DINAH &amp; TOBIAS'S HOME</p>
        <p class="plain">612 North Birch Rd 7B</p>
      </div>
      <div class="notes">
        <p class="strong">COSTUMES HIGHLY ENCOURAGED</p>
        <p class="plain">ADULTS ONLY PLEASE</p>
      </div>
    </section>
  </main>
</body>
</html>
```